Three diagrams for an academic paper

I need professional-looking versions of three diagrams for an academic paper. I am uploading JPEGs of each diagram drafted in Google Docs. I need completely new versions that look much better.

Some detailed requirements:
- Professional styling - must be clearly superior to the ‘stick-figure’ example images and obviously not from powerpoint, etc.
- Must be a coordinated style across all three illustrations.
- Note that a mini-version of figure 2 appears in figure 3 (within the database image)
- I need very high resolution, suitable for a manuscript
- May need some text changes at short notice (anticipate 2 small updates to text)

Target Market(s)

Academics

Industry/Entity Type

Google

Font styles to use
Sans Serif

Colors

Requirements
Must have
• Don't look like powerpoint

```html
<!DOCTYPE html>
<html lang="en">
<head>
<meta charset="utf-8">
<title>Text and annotation granularity</title>
<link href="https://fonts.googleapis.com/css2?family=Lato:wght@400;700;900&display=swap" rel="stylesheet">
<style>
  :root {
    --navy: #00134a;
    --red: #e20a17;
    --paper: #ffffff;
  }
  html, body {
    margin: 0;
    padding: 0;
    width: 1200px;
    height: 362px;
    overflow: hidden;
    background: var(--paper);
  }
  .figure-row {
    position: relative;
    width: 1200px;
    height: 362px;
    font-family: "Lato", sans-serif;
  }
  .variant {
    position: absolute;
    top: 0;
    width: 206px;
  }
  .variant-title {
    position: absolute;
    bottom: calc(100% - 80px);
    left: -30px;
    right: -30px;
    margin: 0;
    text-align: center;
    color: var(--navy);
    font-weight: 900;
    font-size: 15.5px;
    line-height: 18px;
  }
  .granularity-box {
    position: absolute;
    top: 94px;
    left: 0;
    width: 206px;
    height: 207px;
    display: block;
  }
  .glyph-text { font-family: "Lato", sans-serif; font-weight: 700; fill: var(--paper); font-size: 300px; }
  .glyph-data { font-family: "Lato", sans-serif; font-weight: 400; fill: var(--paper); font-size: 112px; letter-spacing: 2px; }
  .fill-text { fill: var(--navy); }
  .fill-data { fill: var(--red); }
  .edge-text { fill: none; stroke: var(--navy); stroke-width: 2; }
  .edge-data { fill: none; stroke: var(--red); stroke-width: 2; }
</style>
</head>
<body>
<main class="figure-row">

  <!-- Article, text only -->
  <section class="variant" style="left:14px">
    <h2 class="variant-title">A text article with no<br>annotation data</h2>
    <svg class="granularity-box" viewBox="0 0 258 258" role="img" aria-label="Full text block, no data block">
      <defs><clipPath id="clip-article-text"><rect x="0" y="0" width="129" height="258"/></clipPath></defs>
      <rect class="fill-text" x="0" y="0" width="129" height="258"/>
      <text class="glyph-text" x="10" y="252" clip-path="url(#clip-article-text)">t</text>
      <rect class="edge-data" x="129" y="1" width="128" height="256"/>
    </svg>
  </section>

  <!-- Article with annotations -->
  <section class="variant" style="left:256px">
    <h2 class="variant-title">A text article with<br>annotation data</h2>
    <svg class="granularity-box" viewBox="0 0 258 258" role="img" aria-label="Large text block with small data block">
      <defs>
        <clipPath id="clip-article-ann-text"><rect x="0" y="0" width="129" height="192"/></clipPath>
        <clipPath id="clip-article-ann-data"><rect x="129" y="0" width="129" height="65"/></clipPath>
      </defs>
      <rect class="edge-text" x="1" y="1" width="128" height="256"/>
      <rect class="edge-data" x="129" y="1" width="128" height="256"/>
      <rect class="fill-text" x="0" y="0" width="129" height="192"/>
      <text class="glyph-text" x="10" y="252" clip-path="url(#clip-article-ann-text)">t</text>
      <rect class="fill-data" x="129" y="0" width="129" height="65"/>
      <text class="glyph-data" x="136" y="110" clip-path="url(#clip-article-ann-data)">01</text>
    </svg>
  </section>

  <!-- Paragraph texteme -->
  <section class="variant" style="left:498px">
    <h2 class="variant-title">A paragraph-size texteme<br>with annotation data</h2>
    <svg class="granularity-box" viewBox="0 0 258 258" role="img" aria-label="Equal text and data blocks">
      <defs>
        <clipPath id="clip-para-text"><rect x="0" y="0" width="129" height="128"/></clipPath>
        <clipPath id="clip-para-data"><rect x="129" y="0" width="129" height="128"/></clipPath>
      </defs>
      <rect class="edge-text" x="1" y="1" width="128" height="256"/>
      <rect class="edge-data" x="129" y="1" width="128" height="256"/>
      <rect class="fill-text" x="0" y="0" width="129" height="128"/>
      <text class="glyph-text" x="10" y="252" clip-path="url(#clip-para-text)">t</text>
      <rect class="fill-data" x="129" y="0" width="129" height="128"/>
      <text class="glyph-data" x="136" y="110" clip-path="url(#clip-para-data)">01</text>
    </svg>
  </section>

  <!-- Sentence micro-texteme -->
  <section class="variant" style="left:740px">
    <h2 class="variant-title">A sentence-size<br>micro-texteme<br>with annotation data</h2>
    <svg class="granularity-box" viewBox="0 0 258 258" role="img" aria-label="Small text block with large data block">
      <defs>
        <clipPath id="clip-sent-text"><rect x="0" y="0" width="129" height="68"/></clipPath>
        <clipPath id="clip-sent-data"><rect x="129" y="0" width="129" height="192"/></clipPath>
      </defs>
      <rect class="edge-text" x="1" y="1" width="128" height="256"/>
      <rect class="edge-data" x="129" y="1" width="128" height="256"/>
      <rect class="fill-text" x="0" y="0" width="129" height="68"/>
      <text class="glyph-text" x="10" y="252" clip-path="url(#clip-sent-text)">t</text>
      <rect class="fill-data" x="129" y="0" width="129" height="192"/>
      <g clip-path="url(#clip-sent-data)">
        <text class="glyph-data" x="136" y="110">01</text>
        <text class="glyph-data" x="136" y="235">10</text>
      </g>
    </svg>
  </section>

  <!-- Structured statement -->
  <section class="variant" style="left:976px">
    <h2 class="variant-title">A structured statement<br>with no text</h2>
    <svg class="granularity-box" viewBox="0 0 258 258" role="img" aria-label="Empty text block, full data block">
      <rect class="edge-text" x="1" y="1" width="128" height="256"/>
      <rect class="fill-data" x="129" y="0" width="129" height="258"/>
      <text class="glyph-data" x="136" y="110">01</text>
      <text class="glyph-data" x="136" y="235">10</text>
    </svg>
  </section>

</main>
</body>
</html>
```